Packaging for Hair Fibers Product

We are a start up company looking for a new packaging design for hair building fibers. These are aimed at predominantly men but also women as well. We already have a logo and i have the packaging design from our competitors. We are wanting to keep the look masculine as 90% of our users will be middle aged men. We would like the colours to be black and white but are open to other colours as well.
It will need to have our logo and the following somewhere on the front.
"Instant Fuller & Thicker Hair" & "Natural Hair Building Fibers" "28g" or "Net Weight 28g"
We only need the front of the packaging designed, please make the other sides of the packaging the same colour but blank.
Target Market(s)
Men 25+
Industry/Entity Type
Hair And Beauty
Requirements
Must have
- Logo which i have included. and the following somewhere on the front.
- "Instant Fuller & Thicker Hair" ; "Natural Hair Building Fibers" "28g" or "Net Weight 28g"
Nice to have
- Make it stand out from the competition or similar to the tarsick example.

```html
<!DOCTYPE html>
<html lang="en">
<head>
<meta charset="utf-8">
<title>Follix Hair Fibers Carton Dieline</title>
<link rel="stylesheet" href="https://fonts.googleapis.com/css2?family=Open+Sans:wght@400;600&display=swap">
<style>
  :root {
    --paper: #ffffff;
    --cut-line: #c4267f;
    --brand-slate: #56627a;
    --band-slate: #75839d;
  }
  html, body {
    margin: 0;
    padding: 0;
    width: 1200px;
    height: 1200px;
    overflow: hidden;
    background: var(--paper);
  }
  .dieline {
    display: block;
    width: 1200px;
    height: 1200px;
  }
  .cut {
    fill: none;
    stroke: var(--cut-line);
    stroke-width: 1;
  }
  .top-band { fill: var(--band-slate); }
  .front-text {
    font-family: "Open Sans", sans-serif;
    fill: var(--brand-slate);
    text-anchor: middle;
  }
  .brand-name { font-size: 19px; letter-spacing: 3px; font-weight: 400; }
  .headline-instant { font-size: 27px; letter-spacing: 1px; }
  .headline-sub { font-size: 10.5px; letter-spacing: 1.6px; }
  .headline-hair { font-size: 54px; letter-spacing: 1px; }
  .tagline { font-size: 9.5px; }
  .net-weight { font-size: 10px; }
</style>
</head>
<body>
<svg class="dieline" viewBox="0 0 880 880" xmlns="http://www.w3.org/2000/svg" aria-label="Flat carton dieline for hair building fibers">
  <!-- colour band across the four body panels -->
  <rect class="top-band" x="40" y="448" width="633" height="14"/>

  <!-- body panels and folds -->
  <g class="cut">
    <rect x="40" y="438" width="633" height="292"/>
    <line x1="198" y1="438" x2="198" y2="730"/>
    <line x1="357" y1="438" x2="357" y2="730"/>
    <line x1="515" y1="438" x2="515" y2="730"/>

    <!-- glue flap -->
    <path d="M673 438 L710 448 V720 L673 730"/>

    <!-- top tuck flap -->
    <path d="M198 438 V244 Q198 234 208 234 H347 Q357 234 357 244 V438"/>
    <line x1="198" y1="278" x2="357" y2="278"/>

    <!-- top dust flaps -->
    <path d="M40 438 V410 L55 398 V358 Q55 346 67 346 H183 V420 L198 438"/>
    <path d="M357 438 L372 420 V346 H488 Q500 346 500 358 V398 L515 410 V438"/>

    <!-- bottom closure -->
    <path d="M40 730 V805 H120 V770 L198 730"/>
    <path d="M198 730 V852 H240 V805 H313 V852 H357 V730"/>
    <path d="M357 730 L435 770 V805 H515 V730"/>
    <path d="M515 730 L555 805 H630 L673 730"/>
  </g>

  <!-- front panel artwork -->
  <g class="front-text">
    <text class="brand-name" x="277" y="490">FOLLIX</text>
    <text class="headline-instant" x="277" y="582">INSTANT</text>
    <text class="headline-sub" x="277" y="596">FULLER &amp; THICKER</text>
    <text class="headline-hair" x="277" y="639">HAIR</text>
    <text class="tagline" x="277" y="652">Natural Hair Building Fibers</text>
    <text class="net-weight" x="277" y="720">28g</text>
  </g>
</svg>
</body>
</html>
```